New Innovative Product needs a new business card design

We need a business card design for a new product line based in Michigan called "Lender TrueCourse." We are a credit company by nature however this product should have a clean, simple, "zorvel-esque" feel. We have a few tag lines we use that could or could not be used...."All Referral Roads Lead to You" we use the attached pic in much or our marketing and also use both a white and/or black logo. Also attached.

We want the image attached on the card in some form or another- the grass/sky image.

Reason: We are extending to go over options with management- (expiring on weekend)

Reason: To finalize our design pick. We will be in touch with the designer of choice within the next day or so...the last few entries have been great- Sorry for the delay.

Reason: Working with a couple different designs trying to get finalized

Reason: Final in the workds

Industry/Entity Type

Marketing

Requirements
Must have
• We want the image attached on the card in some form or another- the grass/sky image.

```html
<!DOCTYPE html>
<html lang="en">
<head>
<meta charset="utf-8">
<title>Lender TrueCourse — Business Card</title>
<link rel="stylesheet" href="https://fonts.googleapis.com/css2?family=Mulish:wght@300;400;600&display=swap">
<style>
  :root {
    --backdrop: #e9e6e1;
    --card-white: #f7f7f7;
    --card-black: #0d0d0d;
    --accent-green: #8fd39a;
    --text-dark: #2b2b2b;
    --text-light: #f1f1f1;
    --sky-blue: #1f5fc0;
    --sky-pale: #bcd6ef;
    --grass-green: #3f8a2a;
    --grass-light: #8cc14e;
  }
  * { margin: 0; padding: 0; box-sizing: border-box; }
  html, body { width: 1200px; height: 1023px; overflow: hidden; }
  body {
    background: var(--backdrop);
    font-family: "Mulish", sans-serif;
    position: relative;
  }
  .card {
    position: absolute;
    width: 640px;
    height: 366px;
    border-radius: 22px;
    overflow: hidden;
    box-shadow: 0 10px 28px rgba(0,0,0,0.25);
  }

  /* Front */
  .card-front { left: 70px; top: 90px; background: var(--card-black); }
  .card-front .divider { position: absolute; inset: 0; }
  .brand {
    position: absolute; left: 40px; top: 70px;
    display: flex; align-items: center; gap: 14px;
  }
  .brand-mark { width: 40px; height: 40px; background: var(--accent-green); }
  .brand-name { font-size: 34px; font-weight: 400; color: var(--text-dark); letter-spacing: -0.5px; }
  .person { position: absolute; right: 40px; top: 44px; text-align: right; }
  .person-name { font-size: 20px; color: var(--accent-green); font-weight: 400; }
  .person-title { font-size: 14px; color: var(--text-dark); }
  .address {
    position: absolute; left: 40px; bottom: 48px;
    font-size: 17px; line-height: 1.3; color: var(--text-light);
  }
  .address .company { color: var(--accent-green); }
  .contacts {
    position: absolute; right: 40px; top: 196px;
    list-style: none; font-size: 15px; color: var(--text-light); line-height: 1.45;
  }
  .contacts li { display: flex; align-items: center; gap: 8px; }
  .contacts svg { width: 14px; height: 14px; flex: none; }
  .rights {
    position: absolute; right: 40px; bottom: 48px;
    font-size: 14px; color: var(--accent-green);
  }

  /* Back */
  .card-back { left: 490px; top: 580px; }
  .landscape {
    position: absolute; inset: 0;
    background: linear-gradient(100deg, var(--grass-green) 0%, var(--grass-light) 30%, var(--sky-pale) 42%, #6fa3dd 62%, var(--sky-blue) 100%);
  }
  .back-brand {
    position: absolute; left: 40px; top: 60px;
    display: flex; align-items: center; gap: 14px;
  }
  .back-brand .brand-mark { background: #d8f0d0; }
  .back-brand .brand-name { color: #ffffff; }
  .division {
    position: absolute; right: 40px; top: 150px;
    font-size: 22px; color: #ffffff;
  }
  .back-url {
    position: absolute; left: 40px; bottom: 40px;
    font-size: 14px; color: #ffffff;
  }
</style>
</head>
<body>

<section class="card card-front" aria-label="Business card front">
  <svg class="divider" viewBox="0 0 640 366" preserveAspectRatio="none" aria-hidden="true">
    <path d="M0 0 H640 V170 H360 L340 186 H0 Z" fill="var(--card-white)"/>
    <path d="M0 186 H340 L360 170 H640 V176 H362 L342 192 H0 Z" fill="var(--accent-green)"/>
  </svg>
  <div class="brand">
    <span class="brand-mark"></span>
    <span class="brand-name">Lender TrueCourse</span>
  </div>
  <div class="person">
    <p class="person-name">Corwin Haleby</p>
    <p class="person-title">Product Manager</p>
  </div>
  <ul class="contacts">
    <li><svg viewBox="0 0 14 14"><rect x="1" y="1" width="12" height="12" rx="2" fill="var(--accent-green)"/><path d="M4 4h2l1 2-1 1 2 2 1-1 2 1v2h-2c-3 0-5-2-5-5z" fill="var(--card-black)"/></svg>555.014.2270</li>
    <li><svg viewBox="0 0 14 14"><rect x="1" y="3" width="12" height="8" fill="var(--accent-green)"/><path d="M1 3l6 5 6-5" stroke="var(--card-black)" fill="none"/></svg>chaleby@ledgerlinesystems.com</li>
    <li><svg viewBox="0 0 14 14"><circle cx="7" cy="7" r="6" fill="var(--accent-green)"/><path d="M1 7h12M7 1v12" stroke="var(--card-black)"/></svg>www.ledgerlinesystems.com</li>
  </ul>
  <address class="address">
    <span class="company">Lender TrueCourse</span><br>
    2716 W. Birchmoor Rd.<br>
    Fenwick, MI 48893
  </address>
  <p class="rights">All rights reserved.</p>
</section>

<section class="card card-back" aria-label="Business card back">
  <div class="landscape" role="img" aria-label="Photograph of a green grass field under a blue sky with white clouds"></div>
  <div class="back-brand">
    <span class="brand-mark"></span>
    <span class="brand-name">Lender TrueCourse</span>
  </div>
  <p class="division">A Division of Ledgerline Systems, Inc.®</p>
  <p class="back-url">www.ledgerlinesystems.com</p>
</section>

</body>
</html>
```